Sophrologist needs a cool signage at door entrance

I need signage for dr in sophrology based in Belgium (french speaking). The signed should capture the name the "Mireille Vantoorn" - "Naturopathe-Sophrologue-Reiki" and a catchphrase = (Healthy way of life)
« Fais du bien à ton corps, pour que ton âme ait envie d’y rester »
Requirements
Must have
- Hey,
Thats the instagram account for some inspiration www.instagram.com/mireille_serene_wellbeing
Light colors, green, blue
Healthy way of life
Size is 45cm wide on 30 cm high
The signage will be placed in front off woof pannel

```html
<!DOCTYPE html>
<html lang="fr">
<head>
<meta charset="utf-8">
<title>Mireille Vantoorn – Signage</title>
<link rel="stylesheet" href="https://fonts.googleapis.com/css2?family=Patrick+Hand&family=Stint+Ultra+Condensed&display=swap">
<style>
  :root {
    --sign-bg: #bafffb;
    --ink-teal: #0d6570;
    --leaf-green: #22dc78;
    --leaf-soft: #9eeec8;
    --skin: #f7dcc8;
    --page-bg: #ffffff;
  }
  html, body {
    margin: 0;
    padding: 0;
    width: 1200px;
    height: 800px;
    overflow: hidden;
    background: var(--page-bg);
  }
  .sign {
    position: relative;
    width: 1200px;
    height: 800px;
    background: var(--sign-bg);
    overflow: hidden;
  }
  .foliage-backdrop {
    position: absolute;
    left: 0;
    top: 0;
    width: 660px;
    height: 520px;
    background: radial-gradient(ellipse at 30% 35%, rgba(158, 238, 200, 0.55), rgba(158, 238, 200, 0) 70%);
  }
  .hand-illustration {
    position: absolute;
    left: 560px;
    top: 220px;
    width: 640px;
    height: 580px;
    background:
      radial-gradient(ellipse at 62% 55%, var(--skin) 0 28%, rgba(247, 220, 200, 0) 42%),
      radial-gradient(ellipse at 80% 60%, var(--leaf-green) 0 30%, rgba(34, 220, 120, 0) 55%),
      radial-gradient(ellipse at 40% 75%, rgba(158, 238, 200, 0.9) 0 25%, rgba(158, 238, 200, 0) 55%);
  }
  .practitioner-name {
    position: absolute;
    left: 58px;
    top: 34px;
    margin: 0;
    font-family: "Patrick Hand", cursive;
    font-weight: 400;
    font-size: 168px;
    line-height: 1;
    letter-spacing: 1px;
    color: var(--ink-teal);
    white-space: nowrap;
  }
  .services {
    position: absolute;
    left: 66px;
    top: 240px;
    margin: 0;
    padding: 0;
    list-style: none;
    font-family: "Stint Ultra Condensed", serif;
    font-size: 122px;
    line-height: 130px;
    color: var(--ink-teal);
  }
  .tagline {
    position: absolute;
    left: 56px;
    top: 650px;
    margin: 0;
    font-family: "Patrick Hand", cursive;
    font-size: 96px;
    line-height: 1;
    color: var(--leaf-green);
    white-space: nowrap;
  }
</style>
</head>
<body>
  <main class="sign">
    <div class="foliage-backdrop" role="img" aria-label="Faint background foliage of fern-like leaves"></div>
    <div class="hand-illustration" role="img" aria-label="Illustration of a decorated hand among green leaves"></div>

    <h1 class="practitioner-name">Mireille Vantoorn</h1>

    <ul class="services">
      <li>Naturopathe</li>
      <li>Sophrologue</li>
      <li>Reiki</li>
    </ul>

    <p class="tagline">Healthy way of life</p>
  </main>
</body>
</html>
```